Order Management User Interface

I need a new design for our order management screens. They need to be end user friendly and contain the data in an easy to read format. These are online orders. I have attached 3 images from the development solution. For now I just need a new UI and ideally would like it delivered in html so we can easily adapt. The screen has multiple tabs to display the different types of data we store. Ideally the end user needs to see customer focused information first.
I have uploaded an example of a different order view that i like.
Fashion Retail
Coded - Design and coding required
1 page

```html
<!DOCTYPE html>
<html lang="en">
<head>
<meta charset="utf-8">
<title>Order Management – Orders and Modal</title>
<link href="https://fonts.googleapis.com/css2?family=Nunito+Sans:wght@300;400;600;700&display=swap" rel="stylesheet">
<style>
:root{
  --bg:#9747c5;
  --frame-a:#3e55ad;
  --frame-b:#8b49c8;
  --panel:#ffffff;
  --panel-soft:#f3f6f9;
  --tabbar:#eef2f6;
  --ink:#262b36;
  --muted:#9aa1ac;
  --line:#e7eaef;
  --brand:#2c4f9e;
  --green:#4bb543;
  --orange:#f5a043;
  --grey:#9097a0;
  --red:#e0435b;
}
*{box-sizing:border-box;margin:0;padding:0}
html,body{width:879px;height:1200px;overflow:hidden;background:var(--bg)}
body{font-family:"Nunito Sans",sans-serif;color:var(--ink)}
.page{position:absolute;left:0;top:0;width:1652px;height:2256px;transform:scale(.5321);transform-origin:0 0;background:var(--bg)}
.section-title{position:absolute;left:238px;font-weight:300;font-size:74px;line-height:1;color:#fff;letter-spacing:.5px}
.frame{position:absolute;left:238px;width:1175px;height:660px;border-radius:14px;overflow:hidden;
  background:linear-gradient(90deg,var(--frame-a),#6a4fc0 55%,var(--frame-b));box-shadow:0 10px 30px rgba(40,10,80,.25)}
.sidebar .brand-name{position:absolute;left:0;top:18px;width:53px;text-align:center;color:#fff;font-weight:700;font-size:11px;line-height:16px}
.sidebar .nav{position:absolute;left:12px;width:30px;height:26px;display:flex;align-items:center;justify-content:center}
.sidebar .nav.active{background:rgba(255,255,255,.14);border-radius:5px}
.sidebar svg{width:13px;height:13px;stroke:#fff;fill:none;stroke-width:1.6;opacity:.55}
.sidebar .active svg{opacity:1}
.panel{position:absolute;left:53px;top:12px;width:1111px;height:637px;border-radius:10px;background:var(--panel);overflow:hidden}
.panel-head{position:absolute;left:0;top:0;width:100%;height:68px;background:var(--panel-soft)}
.panel-title{position:absolute;left:13px;top:12px;font-size:16px;font-weight:700}
.search{position:absolute;left:789px;top:10px;width:273px;height:25px;background:#fff;border-radius:4px;font-size:8px;color:var(--muted);padding:7px 11px}
.search svg{position:absolute;right:10px;top:7px;width:10px;height:10px;stroke:#b6bcc5;fill:none;stroke-width:1.5}
.avatar{position:absolute;left:1075px;top:10px;width:25px;height:25px;border-radius:50%;background:radial-gradient(circle at 40% 40%,#d3663f,#6b2a1c)}
.doc-tabs{position:absolute;left:12px;top:45px;display:flex;font-size:8.5px}
.doc-tab{height:23px;padding:6px 9px;color:var(--muted);width:96px}
.doc-tab.active{background:#fff;color:var(--ink);border-radius:4px 4px 0 0;width:90px}
.doc-tab .x{margin-left:8px;color:#b6bcc5}
.details{position:absolute;left:13px;top:68px;width:134px}
.details-head{display:flex;justify-content:space-between;font-size:9px;padding-top:13px;height:37px}
.details-head .label{font-weight:600}
.field{border-bottom:1px solid var(--line);padding:10px 0 11px;height:51.5px}
.field .k{font-size:7px;color:var(--muted);line-height:10px}
.field .v{font-size:9px;line-height:12px;margin-top:6px}
.field .v.green{color:var(--green);font-weight:600}
.field .v.red{color:var(--red);font-weight:600}
.field.tall{height:74px}
.field .more{color:var(--brand);text-decoration:underline;font-size:8px}
.details-scroll{position:absolute;left:159px;top:68px;width:6px;height:569px;background:#f1f3f6}
.details-scroll i{position:absolute;left:1px;top:2px;width:3px;height:206px;border-radius:2px;background:#c5c9d0}
.status{display:inline-flex;align-items:center;gap:5px;font-size:9px}
.dot{width:9px;height:9px;border-radius:50%;border:1px solid currentColor;position:relative;color:var(--green)}
.dot::after{content:"";position:absolute;left:2px;top:2px;width:3px;height:3px;border-radius:50%;background:currentColor}
.dot.pending{color:var(--orange)}
.dot.cancelled{color:var(--grey)}
.data-tabs{position:absolute;left:177px;top:83px;width:504px;height:25px;background:var(--tabbar);border-radius:3px;display:flex;align-items:center;padding-left:3px;font-size:8px;color:var(--muted)}
.data-tabs span{padding:0 8px}
.data-tabs .active{background:#fff;color:var(--ink);border-radius:3px;height:19px;line-height:19px;padding:0 9px;margin-right:4px}
.toolbar{position:absolute;left:910px;top:83px;height:26px;display:flex;align-items:center;font-size:8px}
.check{width:11px;height:11px;border-radius:2px;background:var(--brand);margin-left:9px;display:flex;align-items:center;justify-content:center}
.check svg{width:8px;height:8px;stroke:#fff;fill:none;stroke-width:2}
.btn-icon{width:25px;height:26px;border-radius:4px;background:#e9edf2;margin-left:14px;display:flex;align-items:center;justify-content:center}
.btn-icon svg{width:11px;height:11px;stroke:#6d7580;fill:none;stroke-width:1.5}
.btn-save{height:26px;width:55px;border-radius:4px;background:var(--brand);color:#fff;margin-left:3px;display:flex;align-items:center;justify-content:center;gap:5px;font-weight:600}
.btn-save svg{width:9px;height:9px;stroke:#fff;fill:none;stroke-width:1.5}
.table{position:absolute;left:177px;top:130px;width:917px}
.grid{display:grid;grid-template-columns:38px 69px 65px 93px 69px 58px 65px 57px 59px 59px 136px 64px 65px 15px;font-size:8.5px}
.thead{height:28px;color:var(--muted);font-size:8px;align-items:center}
.thead .product{grid-column:3/5}
.row{height:46.5px;padding-top:16px;line-height:14px;border-bottom:1px solid var(--line);align-items:start}
.row.open{height:150px}
.plus{color:#8a929d;font-size:14px;line-height:12px;padding-left:10px;font-weight:300}
.sku{color:var(--brand);font-weight:700}
.key{color:var(--muted)}
.strong{font-weight:700}
.spec{grid-column:3/5;display:grid;grid-template-columns:65px 93px;grid-auto-rows:21px;margin-top:-4px}
.spec span:nth-child(odd){color:var(--muted)}
.spec span{line-height:21px}
.chev svg{width:9px;height:9px;stroke:#8a929d;fill:none;stroke-width:1.5;margin-top:3px}
.table-scroll{position:absolute;left:1094px;top:158px;width:3px;height:207px;border-radius:2px;background:#c5c9d0}
.pager{position:absolute;left:1032px;top:603px;font-size:7px;color:var(--muted);display:flex;align-items:center;gap:10px}
.pager svg{width:8px;height:8px;stroke:#8a929d;fill:none;stroke-width:1.5}
.pager svg.next{stroke:var(--ink)}
.overlay{position:absolute;inset:0;background:linear-gradient(100deg,rgba(150,155,225,.62),rgba(190,160,228,.62) 60%,rgba(215,165,225,.65))}
.modal{position:absolute;left:347px;top:35px;width:472px;height:590px;border-radius:10px;background:#fff;overflow:hidden;box-shadow:0 10px 40px rgba(40,20,90,.25)}
.modal-head{height:49px;background:var(--panel-soft);padding:15px 26px;font-size:16px;font-weight:700;position:relative}
.modal-head svg{position:absolute;right:26px;top:20px;width:10px;height:10px;stroke:#8a929d;stroke-width:1.4}
.form{position:relative}
.form-field{position:absolute;width:206px}
.form-field.full{width:424px}
.form-field label{display:block;font-size:7px;color:#5c6470;line-height:10px}
.form-field .input{margin-top:6px;height:25px;border:1px solid var(--line);border-radius:3px;padding:0 11px;font-size:8px;line-height:23px;color:#b3b9c2;position:relative}
.form-field .input.filled{color:var(--ink)}
.form-field .input svg{position:absolute;right:9px;top:8px;width:9px;height:9px;stroke:#6d7580;fill:none;stroke-width:1.5}
.modal-actions{position:absolute;right:23px;bottom:18px;display:flex;gap:4px;font-size:8.5px}
.modal-actions span{height:25px;width:55px;border-radius:3px;display:flex;align-items:center;justify-content:center}
.btn-cancel{background:#eef1f4;color:#555c66}
.btn-update{background:var(--brand);color:#fff;font-weight:600}
</style>
</head>
<body>
<div class="page">

  <h1 class="section-title" style="top:152px">Orders</h1>

  <div class="frame" style="top:328px">
    <div class="sidebar">
      <div class="brand-name">Kivo</div>
      <div class="nav active" style="top:64px"><svg viewBox="0 0 16 16"><path d="M1 2h2l2 8h8l2-6H4"/><circle cx="6" cy="13.5" r="1"/><circle cx="12" cy="13.5" r="1"/></svg></div>
      <div class="nav" style="top:94px"><svg viewBox="0 0 16 16"><path d="M1 5V1h4M11 1h4v4M15 11v4h-4M5 15H1v-4M4 8h8"/></svg></div>
      <div class="nav" style="top:125px"><svg viewBox="0 0 16 16"><path d="M8 15s5-5 5-9a5 5 0 0 0-10 0c0 4 5 9 5 9z"/><circle cx="8" cy="6" r="2"/></svg></div>
      <div class="nav" style="top:157px"><svg viewBox="0 0 16 16"><rect x="2" y="1" width="12" height="14" rx="1"/><circle cx="8" cy="6" r="2"/><path d="M4.5 12c1-2 6-2 7 0"/></svg></div>
      <div class="nav" style="top:187px"><svg viewBox="0 0 16 16"><path d="M1 8s3-5 7-5 7 5 7 5-3 5-7 5-7-5-7-5z"/><circle cx="8" cy="8" r="2"/></svg></div>
      <div class="nav" style="top:217px"><svg viewBox="0 0 16 16"><rect x="2" y="7" width="12" height="8" rx="1"/><path d="M5 7V4a3 3 0 0 1 6 0v3"/></svg></div>
    </div>
    <div class="panel">
      <div class="panel-head"></div>
      <div class="panel-title">Orders</div>
      <div class="search">Search order...<svg viewBox="0 0 12 12"><circle cx="5" cy="5" r="3.8"/><path d="M8 8l3 3"/></svg></div>
      <div class="avatar" role="img" aria-label="User profile photo"></div>
      <div class="doc-tabs">
        <div class="doc-tab active">Order 978393<span class="x">×</span></div>
        <div class="doc-tab">Order 978393<span class="x">×</span></div>
        <div class="doc-tab">Order 978393<span class="x">×</span></div>
      </div>
      <div class="details">
        <div class="details-head"><span class="label">Details</span><span class="status"><i class="dot"></i>New</span></div>
        <div class="field"><div class="k">Order No.</div><div class="v">238923892</div></div>
        <div class="field"><div class="k">Original Order No.</div><div class="v">238923892</div></div>
        <div class="field"><div class="k">Customer No.</div><div class="v">#232</div></div>
        <div class="field"><div class="k">Total Retail</div><div class="v green">105.50</div></div>
        <div class="field tall"><div class="k">Instructions</div><div class="v">Lorem ipsum dolor sit amet, consetetu Lorem ipsum...<br><span class="more">Readmore</span></div></div>
        <div class="field"><div class="k">Brand</div><div class="v">238923892</div></div>
        <div class="field"><div class="k">Reference</div><div class="v">238923892</div></div>
        <div class="field"><div class="k">Full Name</div><div class="v">Test Order</div></div>
        <div class="field"><div class="k">Total Tax</div><div class="v red">9.55</div></div>
        <div class="field"><div class="k">Order Type</div><div class="v">Sale</div></div>
      </div>
      <div class="details-scroll"><i></i></div>
      <div class="data-tabs"><span class="active">Items</span><span>Customer(s)</span><span>Addresses</span><span>Payments</span><span>Vouchers</span><span>Event Queues</span><span>Updates</span><span>Fulfilments</span><span>History</span></div>
      <div class="toolbar">Authority to leave<span class="check"><svg viewBox="0 0 10 10"><path d="M2 5l2 2 4-4"/></svg></span><span class="btn-icon"><svg viewBox="0 0 12 12"><path d="M10 4A4.5 4.5 0 0 0 2 5M2 8a4.5 4.5 0 0 0 8-1M10 1v3H7M2 11V8h3"/></svg></span><span class="btn-save"><svg viewBox="0 0 10 10"><path d="M1 1h6l2 2v6H1zM3 1v3h4V1M3 9V6h4v3"/></svg>Save</span></div>
      <div class="table">
        <div class="grid thead"><span></span><span>SKU</span><span class="product">Product</span><span>Is Dropship</span><span>Quantity</span><span>Unit Retail</span><span>Unit Tax</span><span>Discount</span><span>Final Price</span><span>Discount Reason</span><span>Coupon Code</span><span>Status</span><span></span></div>
        <div class="grid row open"><span class="plus">+</span><span class="sku">2230566</span><div class="spec"><span>Vendor</span><span class="strong" style="color:var(--ink)">Orchard Co</span><span>Brand</span><span>Orchard</span><span>Product Code</span><span>20022569</span><span>Description</span><span>PJ SET</span><span>Colour (Code)</span><span>900</span><span>Size</span><span>12/14</span></div><span>Yes</span><span>23</span><span>35.00</span><span>3.18</span><span>0.00</span><span>35.00</span><span>50% discount for early birds</span><span>324ASD</span><span class="status"><i class="dot"></i>New</span><span class="chev"><svg viewBox="0 0 10 10"><path d="M2 7l3-3 3 3"/></svg></span></div>
        <div class="grid row"><span class="plus">+</span><span class="sku">2323232</span><span class="key">Vendor</span><span class="strong">Keystone</span><span>Yes</span><span>3</span><span>35.00</span><span>3.18</span><span>0.00</span><span>35.00</span><span>50% discount for early birds</span><span>324ASD</span><span class="status"><i class="dot"></i>New</span><span class="chev"><svg viewBox="0 0 10 10"><path d="M2 3l3 3 3-3"/></svg></span></div>
        <div class="grid row"><span class="plus">+</span><span class="sku">4545454</span><span class="key">Vendor</span><span class="strong">Boltline</span><span>No</span><span>23</span><span>35.00</span><span>3.18</span><span>0.00</span><span>35.00</span><span>-</span><span>324ASD</span><span class="status"><i class="dot pending"></i>Pending</span><span class="chev"><svg viewBox="0 0 10 10"><path d="M2 3l3 3 3-3"/></svg></span></div>
        <div class="grid row"><span class="plus">+</span><span class="sku">2230566</span><span class="key">Vendor</span><span class="strong">Sonora</span><span>Yes</span><span>5</span><span>35.00</span><span>3.18</span><span>0.00</span><span>35.00</span><span>-</span><span>324ASD</span><span class="status"><i class="dot pending"></i>Pending</span><span class="chev"><svg viewBox="0 0 10 10"><path d="M2 3l3 3 3-3"/></svg></span></div>
        <div class="grid row"><span class="plus">+</span><span class="sku">6786788</span><span class="key">Vendor</span><span class="strong">Halvik</span><span>No</span><span>23</span><span>35.00</span><span>3.18</span><span>0.00</span><span>35.00</span><span>50% discount for early birds</span><span>324ASD</span><span class="status"><i class="dot"></i>New</span><span class="chev"><svg viewBox="0 0 10 10"><path d="M2 3l3 3 3-3"/></svg></span></div>
        <div class="grid row"><span class="plus">+</span><span class="sku">1282122</span><span class="key">Vendor</span><span class="strong">Mirella</span><span>Yes</span><span>23</span><span>35.00</span><span>3.18</span><span>0.00</span><span>35.00</span><span>-</span><span>324ASD</span><span class="status"><i class="dot cancelled"></i>Cancelled</span><span class="chev"><svg viewBox="0 0 10 10"><path d="M2 3l3 3 3-3"/></svg></span></div>
        <div class="grid row"><span class="plus">+</span><span class="sku">2321329</span><span class="key">Vendor</span><span class="strong">Voltara</span><span>Yes</span><span>23</span><span>35.00</span><span>3.18</span><span>0.00</span><span>35.00</span><span>50% discount for early birds</span><span>324ASD</span><span class="status"><i class="dot"></i>New</span><span class="chev"><svg viewBox="0 0 10 10"><path d="M2 3l3 3 3-3"/></svg></span></div>
      </div>
      <div class="table-scroll"></div>
      <div class="pager">1-10 /100<svg viewBox="0 0 10 10"><path d="M6 2L3 5l3 3"/></svg><svg class="next" viewBox="0 0 10 10"><path d="M4 2l3 3-3 3"/></svg></div>
    </div>
  </div>

  <h1 class="section-title" style="top:1135px">Modal</h1>

  <div class="frame" style="top:1311px">
    <div class="sidebar">
      <div class="brand-name">Kivo</div>
      <div class="nav active" style="top:64px"><svg viewBox="0 0 16 16"><path d="M1 2h2l2 8h8l2-6H4"/><circle cx="6" cy="13.5" r="1"/><circle cx="12" cy="13.5" r="1"/></svg></div>
      <div class="nav" style="top:94px"><svg viewBox="0 0 16 16"><path d="M1 5V1h4M11 1h4v4M15 11v4h-4M5 15H1v-4M4 8h8"/></svg></div>
      <div class="nav" style="top:125px"><svg viewBox="0 0 16 16"><path d="M8 15s5-5 5-9a5 5 0 0 0-10 0c0 4 5 9 5 9z"/><circle cx="8" cy="6" r="2"/></svg></div>
      <div class="nav" style="top:157px"><svg viewBox="0 0 16 16"><rect x="2" y="1" width="12" height="14" rx="1"/><circle cx="8" cy="6" r="2"/><path d="M4.5 12c1-2 6-2 7 0"/></svg></div>
      <div class="nav" style="top:187px"><svg viewBox="0 0 16 16"><path d="M1 8s3-5 7-5 7 5 7 5-3 5-7 5-7-5-7-5z"/><circle cx="8" cy="8" r="2"/></svg></div>
      <div class="nav" style="top:217px"><svg viewBox="0 0 16 16"><rect x="2" y="7" width="12" height="8" rx="1"/><path d="M5 7V4a3 3 0 0 1 6 0v3"/></svg></div>
    </div>
    <div class="panel">
      <div class="panel-head"></div>
      <div class="panel-title">Orders</div>
      <div class="search">Search order...<svg viewBox="0 0 12 12"><circle cx="5" cy="5" r="3.8"/><path d="M8 8l3 3"/></svg></div>
      <div class="avatar" role="img" aria-label="User profile photo"></div>
      <div class="doc-tabs">
        <div class="doc-tab active">Order 978393<span class="x">×</span></div>
        <div class="doc-tab">Order 978393<span class="x">×</span></div>
        <div class="doc-tab">Order 978393<span class="x">×</span></div>
      </div>
      <div class="details">
        <div class="details-head"><span class="label">Details</span><span class="status"><i class="dot"></i>New</span></div>
        <div class="field"><div class="k">Order No.</div><div class="v">238923892</div></div>
        <div class="field"><div class="k">Original Order No.</div><div class="v">238923892</div></div>
        <div class="field"><div class="k">Customer No.</div><div class="v">#232</div></div>
        <div class="field"><div class="k">Total Retail</div><div class="v green">105.50</div></div>
        <div class="field tall"><div class="k">Instructions</div><div class="v">Lorem ipsum dolor sit amet, consetetu Lorem ipsum...<br><span class="more">Readmore</span></div></div>
        <div class="field"><div class="k">Brand</div><div class="v">238923892</div></div>
        <div class="field"><div class="k">Reference</div><div class="v">238923892</div></div>
        <div class="field"><div class="k">Full Name</div><div class="v">Test Order</div></div>
        <div class="field"><div class="k">Total Tax</div><div class="v red">9.55</div></div>
        <div class="field"><div class="k">Order Type</div><div class="v">Sale</div></div>
      </div>
      <div class="details-scroll"><i></i></div>
      <div class="data-tabs"><span class="active">Items</span><span>Customer(s)</span><span>Addresses</span><span>Payments</span><span>Vouchers</span><span>Event Queues</span><span>Updates</span><span>Fulfilments</span><span>History</span></div>
      <div class="toolbar">Authority to leave<span class="check"><svg viewBox="0 0 10 10"><path d="M2 5l2 2 4-4"/></svg></span><span class="btn-icon"><svg viewBox="0 0 12 12"><path d="M10 4A4.5 4.5 0 0 0 2 5M2 8a4.5 4.5 0 0 0 8-1M10 1v3H7M2 11V8h3"/></svg></span><span class="btn-save"><svg viewBox="0 0 10 10"><path d="M1 1h6l2 2v6H1zM3 1v3h4V1M3 9V6h4v3"/></svg>Save</span></div>
      <div class="table">
        <div class="grid thead"><span></span><span>SKU</span><span class="product">Product</span><span>Is Dropship</span><span>Quantity</span><span>Unit Retail</span><span>Unit Tax</span><span>Discount</span><span>Final Price</span><span>Discount Reason</span><span>Coupon Code</span><span>Status</span><span></span></div>
        <div class="grid row open"><span class="plus">+</span><span class="sku">2230566</span><div class="spec"><span>Vendor</span><span class="strong" style="color:var(--ink)">Orchard Co</span><span>Brand</span><span>Orchard</span><span>Product Code</span><span>20022569</span><span>Description</span><span>PJ SET</span><span>Colour (Code)</span><span>900</span><span>Size</span><span>12/14</span></div><span>Yes</span><span>23</span><span>35.00</span><span>3.18</span><span>0.00</span><span>35.00</span><span>50% discount for early birds</span><span>324ASD</span><span class="status"><i class="dot"></i>New</span><span class="chev"><svg viewBox="0 0 10 10"><path d="M2 7l3-3 3 3"/></svg></span></div>
        <div class="grid row"><span class="plus">+</span><span class="sku">2323232</span><span class="key">Vendor</span><span class="strong">Keystone</span><span>Yes</span><span>3</span><span>35.00</span><span>3.18</span><span>0.00</span><span>35.00</span><span>50% discount for early birds</span><span>324ASD</span><span class="status"><i class="dot"></i>New</span><span class="chev"><svg viewBox="0 0 10 10"><path d="M2 3l3 3 3-3"/></svg></span></div>
        <div class="grid row"><span class="plus">+</span><span class="sku">4545454</span><span class="key">Vendor</span><span class="strong">Boltline</span><span>No</span><span>23</span><span>35.00</span><span>3.18</span><span>0.00</span><span>35.00</span><span>-</span><span>324ASD</span><span class="status"><i class="dot pending"></i>Pending</span><span class="chev"><svg viewBox="0 0 10 10"><path d="M2 3l3 3 3-3"/></svg></span></div>
        <div class="grid row"><span class="plus">+</span><span class="sku">2230566</span><span class="key">Vendor</span><span class="strong">Sonora</span><span>Yes</span><span>5</span><span>35.00</span><span>3.18</span><span>0.00</span><span>35.00</span><span>-</span><span>324ASD</span><span class="status"><i class="dot pending"></i>Pending</span><span class="chev"><svg viewBox="0 0 10 10"><path d="M2 3l3 3 3-3"/></svg></span></div>
        <div class="grid row"><span class="plus">+</span><span class="sku">6786788</span><span class="key">Vendor</span><span class="strong">Halvik</span><span>No</span><span>23</span><span>35.00</span><span>3.18</span><span>0.00</span><span>35.00</span><span>50% discount for early birds</span><span>324ASD</span><span class="status"><i class="dot"></i>New</span><span class="chev"><svg viewBox="0 0 10 10"><path d="M2 3l3 3 3-3"/></svg></span></div>
        <div class="grid row"><span class="plus">+</span><span class="sku">1282122</span><span class="key">Vendor</span><span class="strong">Mirella</span><span>Yes</span><span>23</span><span>35.00</span><span>3.18</span><span>0.00</span><span>35.00</span><span>-</span><span>324ASD</span><span class="status"><i class="dot cancelled"></i>Cancelled</span><span class="chev"><svg viewBox="0 0 10 10"><path d="M2 3l3 3 3-3"/></svg></span></div>
        <div class="grid row"><span class="plus">+</span><span class="sku">2321329</span><span class="key">Vendor</span><span class="strong">Voltara</span><span>Yes</span><span>23</span><span>35.00</span><span>3.18</span><span>0.00</span><span>35.00</span><span>50% discount for early birds</span><span>324ASD</span><span class="status"><i class="dot"></i>New</span><span class="chev"><svg viewBox="0 0 10 10"><path d="M2 3l3 3 3-3"/></svg></span></div>
      </div>
      <div class="table-scroll"></div>
      <div class="pager">1-10 /100<svg viewBox="0 0 10 10"><path d="M6 2L3 5l3 3"/></svg><svg class="next" viewBox="0 0 10 10"><path d="M4 2l3 3-3 3"/></svg></div>
    </div>
    <div class="overlay"></div>

    <div class="modal" role="dialog" aria-label="Edit address">
      <div class="modal-head">Orders<svg viewBox="0 0 10 10"><path d="M1 1l8 8M9 1l-8 8"/></svg></div>
      <div class="form">
        <div class="form-field" style="left:26px;top:21px"><label>First Name</label><div class="input filled">Test</div></div>
        <div class="form-field" style="left:244px;top:21px"><label>Sur Name</label><div class="input filled">Order</div></div>
        <div class="form-field" style="left:26px;top:81px"><label>Attention of</label><div class="input">Enter attention of</div></div>
        <div class="form-field full" style="left:26px;top:140px"><label>Address 1</label><div class="input">Enter address</div></div>
        <div class="form-field full" style="left:26px;top:200px"><label>Address 2</label><div class="input">Enter address</div></div>
        <div class="form-field" style="left:26px;top:259px"><label>Suburb</label><div class="input">Enter Suburb</div></div>
        <div class="form-field" style="left:244px;top:259px"><label>City</label><div class="input">Enter City</div></div>
        <div class="form-field" style="left:26px;top:318px"><label>Postcode</label><div class="input">Enter Postcode</div></div>
        <div class="form-field" style="left:244px;top:318px"><label>Country</label><div class="input">Enter Country<svg viewBox="0 0 10 10"><path d="M2 3l3 3 3-3"/></svg></div></div>
        <div class="form-field full" style="left:26px;top:378px"><label>Email</label><div class="input">Enter email</div></div>
        <div class="form-field" style="left:26px;top:437px"><label>Phone</label><div class="input">Enter Phone</div></div>
      </div>
      <div class="modal-actions"><span class="btn-cancel">Cancel</span><span class="btn-update">Update</span></div>
    </div>
  </div>

</div>
</body>
</html>
```